Letterhead design for Dental Practice - Ashby Lane Dental Care

Letterhead for Private Dental Practice. To be used for all official correspondance and for printing treatment details on to be given to patients.

Target Market(s)

Private dental patients

Industry/Entity Type

Dental Clinic

Font styles to use
Other font styles liked:
• nexa-light

Colors
33a6d7
1c66ac
85abd2

Requirements
Must have
• info in the footer and header needs to be 3.5cm from upper/lower boader of paper, see photo in uploaded files
• info details:
• tel. 0115 947 3051
• email info@ashbylanedc.co.uk
• ashbylanedentalcare.co.uk
• 17b Ashby Lane Elmsworth Kenfield KF4 7QT
• nexa-light font as in uploaded logo files
Should not have
• No funny tooth pictures

```html
<!DOCTYPE html>
<html lang="en">
<head>
<meta charset="utf-8">
<title>Ashby Lane Dental Care – Letterhead</title>
<link rel="stylesheet" href="https://fonts.googleapis.com/css2?family=Quicksand:wght@400;700&display=swap">
<style>
  :root {
    --brand-light: #33a6d7;
    --brand-deep: #1c66ac;
    --brand-soft: #85abd2;
    --paper: #ffffff;
    --backdrop: #d6d6d6;
  }
  * { box-sizing: border-box; margin: 0; padding: 0; }
  html, body {
    width: 1200px;
    height: 1000px;
    overflow: hidden;
    background: var(--backdrop);
    font-family: "Quicksand", sans-serif;
  }
  .letterhead {
    position: absolute;
    left: 290px;
    top: 50px;
    width: 620px;
    height: 900px;
    background: var(--paper);
    box-shadow: 0 4px 14px rgba(0,0,0,0.18);
  }
  .brand {
    position: absolute;
    left: 60px;
    top: 70px;
    display: flex;
    align-items: center;
    gap: 12px;
  }
  .brand-dot {
    width: 28px;
    height: 28px;
    border-radius: 50%;
    background: var(--brand-light);
    flex: none;
  }
  .brand-name {
    font-size: 26px;
    font-weight: 400;
    color: var(--brand-light);
    letter-spacing: 0.3px;
    line-height: 1;
    white-space: nowrap;
  }
  .contact {
    position: absolute;
    left: 50px;
    bottom: 44px;
  }
  .contact-address {
    font-size: 12.5px;
    font-weight: 700;
    color: var(--brand-deep);
    line-height: 1.3;
    margin-bottom: 14px;
    white-space: nowrap;
  }
  .contact-list { list-style: none; }
  .contact-item {
    display: flex;
    align-items: center;
    gap: 8px;
    font-size: 13px;
    font-weight: 400;
    color: var(--brand-light);
    line-height: 1;
    margin-bottom: 11px;
    white-space: nowrap;
  }
  .contact-item:last-child { margin-bottom: 0; }
  .contact-icon {
    width: 10px;
    height: 10px;
    fill: var(--brand-deep);
    flex: none;
  }
</style>
</head>
<body>
  <main class="letterhead">
    <header class="brand">
      <span class="brand-dot"></span>
      <span class="brand-name">Ashby Lane Dental Care</span>
    </header>

    <footer class="contact">
      <p class="contact-address">17b Ashby Lane Elmsworth<br>Kenfield KF4 7QT</p>
      <ul class="contact-list">
        <li class="contact-item">
          <svg class="contact-icon" viewBox="0 0 10 10" aria-hidden="true">
            <path d="M2 0.5 L3.6 2.6 L2.7 3.6 Q3.6 5.6 6.4 7.3 L7.4 6.4 L9.5 8 L8.3 9.5 Q4.5 9 0.5 1.7 Z"/>
          </svg>
          0115 947 3051
        </li>
        <li class="contact-item">
          <svg class="contact-icon" viewBox="0 0 10 10" aria-hidden="true">
            <path d="M0.5 2.5 H9.5 V8 H0.5 Z M0.5 2.5 L5 5.8 L9.5 2.5" stroke="#ffffff" stroke-width="0.6"/>
          </svg>
          info@ashbylanedc.co.uk
        </li>
        <li class="contact-item">
          <svg class="contact-icon" viewBox="0 0 10 10" aria-hidden="true">
            <circle cx="5" cy="5" r="4.6"/>
            <path d="M0.6 5 H9.4 M5 0.4 Q2.6 5 5 9.6 M5 0.4 Q7.4 5 5 9.6" stroke="#ffffff" stroke-width="0.6" fill="none"/>
          </svg>
          ashbylanedentalcare.co.uk
        </li>
      </ul>
    </footer>
  </main>
</body>
</html>
```